Postcard: Open Sky Circle

Text for front: HOW TO CHANGE THE WORLD IN ONE [note: the word "one" should be underlined] STEPHint: It's up to you...[Note: add arrow or something to indicate "turn over"]Text for back: You're going to spend your entire life with someone you can never get away from. (Guess who?) Wouldn't you rather that person #OpenSkyCircle than judgmental or critical? BE the change you want to see! Visit www.OpenSkyCircle-hub.example for daily Dawn Pebbles and community. PLEASE JOIN US![Note: add logo to left half of back side]Font preference for text: Josefin sans

Target Market(s)

People who would be attracted to Corvane church - teravian perennist message. It's spiritual without being overtly religious, so the target market is probably early 30s and up but ideally won't turn off Millennials (folks under 30). It should attract attention of people who are open-minded and committed to progressive social change, tired of an atmosphere of hate-mongering and divisiveness.

Requirements
Nice to have
• It would be nice to convey a sense of challenge - there is an idea of "dawn pebbles" so something related to fire/sparks is appropriate. This is meant to evoke a deeper, divine love more than a sense of romantic love. This love is more fierce than fluffy! Yet it calls us to be our best selves.
Should not have
• Please avoid excessive pink - just the logo is enough, as this design needs to appeal to men as well as women.

```html
<!DOCTYPE html>
<html lang="en">
<head>
<meta charset="utf-8">
<title>Open Sky Circle – Postcard</title>
<link rel="stylesheet" href="https://fonts.googleapis.com/css2?family=Josefin+Sans:wght@300;400;600;700&display=swap">
<style>
  :root {
    --backdrop: #3f3f3f;
    --paper: #ffffff;
    --wash-deep: #e8505f;
    --wash-mid: #ee7a86;
    --wash-light: #f4a9b1;
    --ink-pink: #d9457a;
    --soft-pink: #f2b6cb;
    --turn-pink: #f0a7bd;
  }
  * { margin: 0; padding: 0; box-sizing: border-box; }
  html, body {
    width: 866px; height: 1200px; overflow: hidden;
    background: var(--backdrop);
    font-family: "Josefin Sans", sans-serif;
  }
  .postcard {
    position: absolute; left: 66px; width: 733px;
    box-shadow: 0 22px 30px rgba(0,0,0,0.35);
  }
  /* Front */
  .postcard--front { top: 72px; height: 483px; overflow: hidden; }
  .front-wash {
    position: absolute; inset: 0;
    background:
      radial-gradient(ellipse 60% 50% at 25% 55%, var(--wash-deep), transparent 70%),
      radial-gradient(ellipse 50% 60% at 80% 30%, var(--wash-light), transparent 70%),
      linear-gradient(120deg, var(--wash-mid), var(--wash-light) 55%, var(--wash-mid));
  }
  .front-title {
    position: absolute; left: 60px; top: 50px;
    color: var(--paper); font-weight: 300; font-size: 60px;
    line-height: 70px; letter-spacing: 1px;
  }
  .front-title .emphasis-one {
    font-weight: 600; text-decoration: underline;
    text-decoration-thickness: 4px; text-underline-offset: 10px;
  }
  .front-title .emphasis-step { font-weight: 600; }
  .front-hint {
    position: absolute; left: 73px; top: 402px;
    color: var(--paper); font-weight: 600; font-size: 31px;
  }
  .page-curl { position: absolute; right: 0; bottom: 0; }
  .turn-label {
    position: absolute; right: 32px; bottom: 25px;
    color: var(--turn-pink); font-weight: 600; font-size: 14px; letter-spacing: 0.5px;
  }
  /* Back */
  .postcard--back { top: 630px; height: 487px; background: var(--paper); }
  .brand-block {
    position: absolute; left: 40px; top: 40px; width: 330px; height: 330px;
    display: flex; align-items: center; justify-content: center; gap: 12px;
  }
  .brand-dot { width: 18px; height: 18px; border-radius: 50%; background: var(--ink-pink); }
  .brand-name { color: var(--ink-pink); font-weight: 300; font-size: 36px; letter-spacing: 1px; }
  .back-copy {
    position: absolute; left: 408px; top: 60px; width: 310px;
    color: var(--ink-pink); font-weight: 300; font-size: 17px; line-height: 22px;
  }
  .back-copy .guess {
    font-weight: 600; font-size: 31px; line-height: 36px; margin: 14px 0 4px;
  }
  .back-copy .site { font-weight: 700; }
  .join-us {
    position: absolute; left: 0; right: 0; top: 397px; text-align: center;
    color: var(--soft-pink); font-weight: 600; font-size: 58px; letter-spacing: 3px;
  }
</style>
</head>
<body>
  <section class="postcard postcard--front">
    <div class="front-wash" role="img" aria-label="Soft red and pink watercolour wash background"></div>
    <h1 class="front-title">HOW TO CHANGE<br>THE WORLD<br>IN <span class="emphasis-one">ONE</span> <span class="emphasis-step">STEP</span></h1>
    <p class="front-hint">Hint: It’s up to you...</p>
    <svg class="page-curl" width="260" height="225" viewBox="0 0 260 225" aria-hidden="true">
      <defs>
        <linearGradient id="flap" x1="0" y1="1" x2="1" y2="0">
          <stop offset="0" stop-color="#ffffff"/>
          <stop offset="0.6" stop-color="#e9e9e9"/>
          <stop offset="1" stop-color="#9a9a9a"/>
        </linearGradient>
      </defs>
      <path d="M0 225 C70 215 110 190 150 150 C195 105 235 55 260 0 L260 225 Z" fill="#ffffff"/>
      <path d="M0 225 C70 215 110 190 150 150 C195 105 235 55 260 0 C245 50 225 75 190 82 C165 88 150 105 145 135 C138 175 110 205 0 225 Z" fill="url(#flap)"/>
    </svg>
    <span class="turn-label">PLEASE TURN</span>
  </section>

  <section class="postcard postcard--back">
    <div class="brand-block">
      <span class="brand-dot"></span>
      <span class="brand-name">Open Sky Circle</span>
    </div>
    <div class="back-copy">
      <p>You’re going to spend your entire life with someone you can never get away from.</p>
      <p class="guess">(Guess who?)</p>
      <p>Wouldn’t you rather that person #OpenSkyCircle than judgmental or critical? BE the change you want to see!</p>
      <p>Visit <span class="site">www.OpenSkyCircle-hub.example</span> for daily Dawn Pebbles and community.</p>
    </div>
    <p class="join-us">PLEASE JOIN US!</p>
  </section>
</body>
</html>
```